Talent Harbor Posts - Built for the Industry, by the Industry.

Looking for an email marketing Infographic I can send out via email to target Recruitment Firms letting them know we are launched! As of January 7th VORANTE is no longer allowing Recruitment Firms to post on their site unless you pay thousands of dollars a month. We are launching a site just for Recruiters to showcase their jobs. I have attached the almost completed website and a mocked up version of a simple infographic but we are looking for a WOW design that can get emailed out to 1000's of Recruitment Firms and they will just have to click the image to be taken to our site. I have added the colors and raleway - medium is the font on our site. Blue RGB: 8/113/182 Navy RGB: 27/32/48

Recruitment Firms Across Canada and the USA

• WOW Factor, use of our Brand and Colours - raleway - medium is the font on our site. Blue RGB: 8/113/182 Navy RGB: 27/32/48. Our Logo and I have also attached our Landing Page ... down below.
• You can use "It's Time for Something New" or I'd be open to other ideas and taglines ... I'd like to see No Sponsored Jobs / No Pay-Per-Click / Flat Rates Only ...
• Our tagline is also - Built for the Industry, by the Industry"

```html
<!DOCTYPE html>
<html lang="en">
<head>
<meta charset="utf-8">
<title>Talent Harbor Posts – It's Time for Something New</title>
<link href="https://fonts.googleapis.com/css2?family=Raleway:wght@300;400;500;700;800&display=swap" rel="stylesheet">
<style>
  :root {
    --navy: #1b2030;
    --navy-deep: #161a28;
    --navy-soft: #222840;
    --brand-blue: #0871b6;
    --orange: #f7931e;
    --orange-deep: #e07a0c;
    --white: #ffffff;
    --button-rim: #8a8d93;
    --button-text: #2a1c08;
  }
  * { box-sizing: border-box; margin: 0; padding: 0; }
  html, body {
    width: 909px;
    height: 1200px;
    overflow: hidden;
    background: var(--navy);
  }
  .email {
    position: relative;
    width: 909px;
    height: 1200px;
    background: linear-gradient(160deg, var(--navy-soft) 0%, var(--navy) 45%, var(--navy-deep) 100%);
    font-family: 'Raleway', sans-serif;
    color: var(--white);
    text-align: center;
  }
  .brand {
    position: absolute;
    top: 150px;
    left: 0;
    width: 100%;
    display: flex;
    justify-content: center;
    align-items: center;
    gap: 22px;
  }
  .brand-mark {
    width: 70px;
    height: 70px;
    border-radius: 50%;
    background: var(--white);
  }
  .brand-name {
    font-weight: 500;
    font-size: 44px;
    letter-spacing: 3px;
    line-height: 1.05;
    text-align: left;
    text-transform: uppercase;
  }
  .rule {
    position: absolute;
    left: 50%;
    height: 2px;
    background: var(--brand-blue);
    transform: translateX(-50%);
  }
  .rule-top { top: 324px; width: 610px; }
  .rule-bottom { top: 750px; width: 450px; }
  .headline {
    position: absolute;
    top: 352px;
    left: 0;
    width: 100%;
  }
  .headline-lead {
    display: block;
    font-weight: 300;
    font-size: 84px;
    line-height: 1;
    color: var(--orange);
  }
  .headline-main {
    display: block;
    margin-top: 6px;
    font-weight: 800;
    font-size: 66px;
    line-height: 1;
    letter-spacing: -0.5px;
  }
  .benefits {
    position: absolute;
    top: 540px;
    left: 0;
    width: 100%;
    list-style: none;
  }
  .benefit {
    display: flex;
    justify-content: center;
    align-items: center;
    gap: 18px;
    height: 68px;
    font-weight: 400;
    font-size: 40px;
  }
  .benefit svg { width: 50px; height: 50px; flex: none; }
  .cta {
    position: absolute;
    top: 800px;
    left: 50%;
    transform: translateX(-50%);
    width: 266px;
    height: 92px;
    padding: 4px;
    border-radius: 5px;
    background: var(--button-rim);
  }
  .cta-face {
    display: flex;
    align-items: center;
    justify-content: center;
    width: 100%;
    height: 100%;
    border-radius: 3px;
    background: linear-gradient(180deg, var(--orange) 0%, var(--orange-deep) 100%);
    color: var(--button-text);
    font-weight: 700;
    font-size: 40px;
    text-decoration: none;
  }
  .pitch {
    position: absolute;
    top: 944px;
    left: 50%;
    transform: translateX(-50%);
    width: 370px;
    font-weight: 500;
    font-size: 18px;
    line-height: 1.28;
    letter-spacing: 3px;
    text-transform: uppercase;
  }
  .site-url {
    position: absolute;
    top: 1092px;
    left: 0;
    width: 100%;
    font-weight: 500;
    font-size: 19px;
    letter-spacing: 2.5px;
  }
</style>
</head>
<body>
  <main class="email">
    <header class="brand">
      <span class="brand-mark" aria-hidden="true"></span>
      <span class="brand-name">Talent Harbor<br>Posts</span>
    </header>

    <div class="rule rule-top"></div>

    <h1 class="headline">
      <span class="headline-lead">IT'S TIME FOR</span>
      <span class="headline-main">SOMETHING NEW</span>
    </h1>

    <ul class="benefits">
      <li class="benefit">
        <svg viewBox="0 0 50 50" aria-hidden="true">
          <circle cx="25" cy="25" r="21" fill="none" stroke="#f7931e" stroke-width="3"/>
          <line x1="10" y1="10" x2="40" y2="40" stroke="#f7931e" stroke-width="3"/>
        </svg>
        No sponsored jobs
      </li>
      <li class="benefit">
        <svg viewBox="0 0 50 50" aria-hidden="true">
          <circle cx="25" cy="25" r="21" fill="none" stroke="#f7931e" stroke-width="3"/>
          <line x1="40" y1="10" x2="10" y2="40" stroke="#f7931e" stroke-width="3"/>
        </svg>
        No pay-per-click
      </li>
      <li class="benefit">
        <svg viewBox="0 0 50 50" aria-hidden="true">
          <circle cx="25" cy="25" r="21" fill="none" stroke="#f7931e" stroke-width="3"/>
          <text x="25" y="34" text-anchor="middle" font-family="Raleway, sans-serif" font-weight="700" font-size="26" fill="#f7931e">$</text>
        </svg>
        Flat rates only
      </li>
    </ul>

    <div class="rule rule-bottom"></div>

    <div class="cta">
      <a class="cta-face" href="#">Contact Us</a>
    </div>

    <p class="pitch">Let our vast network of recruiters connect you with your next opportunity.</p>

    <p class="site-url">www.talentharborposts.com</p>
  </main>
</body>
</html>
```